Childrens Development/Fun Centre needs a Kid-Centric website

We need a website devoted to what we love, children, this site should be similar to other children development centre website which offer similar services and developments (best example - m o s s y p e r c h . c o . u k)

We need to reflect our values of being fun and friendly whilst also imparting important skills and knowledge onto children. The website should have a button at the top for login (we are using the same MIS system as the example website listed above - so the login and members pages will be hosted by a third party site).

The site should incorporate a like us on chatterdeck button, a snapwheel feed (please only use cobalt framedeck plugin for the snapwheel, for the quibbly you can just use the standard code from quibbly no need for a plugin)

We need to have postwren on the site too with a form to join our mailing list.

Initially we want to see some nice designs which are similar in feel and vibe of the logo which is enclosed, in a format the same as the example listed above.

thanks

Reason: Hi, Apologies for the delay and the miscommunication, we need this website actually CODED, the design can be directly based on the design of the website mentioned in the brief. please only submit or send me a message if your proposal was for CODING! thanks

```html
<!DOCTYPE html>
<html lang="en">
<head>
<meta charset="utf-8">
<title>Sproutyard – Fun Centre for Childrens Development</title>
<link href="https://fonts.googleapis.com/css2?family=Open+Sans:ital,wght@0,400;0,600;0,700;1,400;1,600&display=swap" rel="stylesheet">
<style>
:root{
  --page-bg:#a8d777;
  --white:#ffffff;
  --green:#0ba152;
  --blue:#27b6d8;
  --lime:#7cc242;
  --pink:#e6479b;
  --orange:#f6aa33;
  --navy:#2d2b8d;
  --purple:#5b3f93;
  --text:#4a4a4a;
  --rule:#dcdcdc;
  --field:#f1f1f1;
}
*{box-sizing:border-box;margin:0;padding:0}
html,body{width:1192px;height:1200px;overflow:hidden}
body{background:var(--page-bg);font-family:"Open Sans",Arial,sans-serif;color:var(--text);position:relative}
.site{position:absolute;left:207px;top:0;width:778px;height:1200px;background:var(--white)}
.abs{position:absolute}
.ph{position:absolute}

/* header */
.brand{left:4px;top:64px;width:270px;font-size:43px;font-weight:700;color:var(--green);letter-spacing:-1px;line-height:1;white-space:nowrap}
.social{top:0;left:622px;display:flex;gap:4px}
.social span{width:19px;height:20px;display:block}
.social .s1{background:var(--navy)}
.social .s2{background:var(--blue)}
.social .s3{background:#8a6a4f}
.member-login{left:693px;top:0;width:85px;height:20px;background:var(--green);color:#fff;font-size:10.5px;font-weight:600;text-align:center;line-height:20px}
.nav{position:absolute;top:89px;left:0;width:778px;height:70px;z-index:5}
.tab{position:absolute;top:0;height:64px;border-radius:5px 5px 0 0;color:#fff;font-weight:700;font-size:13.5px;text-align:center;padding-top:13px}
.tab.home{left:374px;width:67px;background:var(--green);height:66px}
.tab.about{left:446px;width:69px;background:var(--blue);height:48px}
.tab.activities{left:520px;width:87px;background:var(--lime);height:44px}
.tab.services{left:613px;width:80px;background:var(--pink);height:40px}
.tab.contact{left:699px;width:79px;background:var(--orange);height:60px}

/* hero */
.hero{left:0;top:131px;width:778px;height:425px;background:linear-gradient(100deg,#4d7a2e 0%,#c99b7a 22%,#e8c6a8 40%,#d9b79a 58%,#b9c3a2 78%,#e9ece0 100%);overflow:hidden}
.hero-curve{position:absolute;left:0;top:131px;z-index:4}
.hanging-kid{left:532px;top:77px;width:131px;height:375px;background:linear-gradient(180deg,#d6b08c 0%,#e7e09a 35%,#6b6a4f 70%,#9e9b86 100%);border-radius:30px;z-index:3}

/* welcome */
.welcome-title{left:17px;top:566px;font-size:17px;font-weight:600;color:var(--green)}
.welcome-rule{left:17px;top:594px;width:538px;height:1px;background:var(--rule)}
.welcome-copy{left:17px;top:601px;width:545px;font-size:10.1px;line-height:15.5px}
.welcome-copy p{margin-bottom:6px}
.welcome-copy b{color:#333}
.welcome-photo{left:576px;top:572px;width:186px;height:137px;border:2px solid var(--green);padding:3px}
.welcome-photo div{width:100%;height:100%;background:linear-gradient(135deg,#a2b7a0,#d9b596 55%,#8fc3d6)}

/* activities */
.fun-title{left:15px;top:726px;font-size:17px;font-weight:600;color:var(--green)}
.thumbs{left:15px;top:758px;display:flex;gap:8px}
.thumb{width:143px}
.thumb .pic{height:122px;border:2px solid #35b77a;padding:2px}
.thumb .pic div{width:100%;height:100%}
.thumb p{margin-top:5px;font-size:11.8px;color:var(--navy)}
.t1{background:linear-gradient(135deg,#8aa07e,#dcb08e)}
.t2{background:linear-gradient(135deg,#7eaa4f,#e2c2a0 55%,#78b54c)}
.t3{background:linear-gradient(135deg,#3a3a3a,#e7b183 50%,#c9483a)}
.t4{background:linear-gradient(135deg,#6f8a6d,#c8b9a1 55%,#e2a2a2)}
.t5{background:linear-gradient(135deg,#d9dfe0,#c3a486 55%,#57b7c8)}

/* cards */
.card-back,.card{position:absolute}
.card{padding:12px 12px 0 12px;color:#fff}
.card h2{font-size:15.5px;font-weight:600;margin-bottom:12px}
.btn{position:absolute;font-size:9.5px;font-style:italic;font-weight:600;color:#fff;text-align:center;line-height:17px;height:17px;clip-path:polygon(8% 0,100% 0,92% 100%,0 100%)}

.testimonial-back{left:10px;top:928px;width:247px;height:208px;background:var(--lime);transform:rotate(-2deg)}
.testimonial{left:17px;top:930px;width:237px;height:208px;background:var(--pink);transform:rotate(1.2deg)}
.avatar{position:absolute;left:10px;top:34px;width:86px;height:86px;border-radius:50%;border:3px solid #fff;background:linear-gradient(135deg,#f3d9c7,#c58f7a 60%,#8fbfd8)}
.who{position:absolute;left:106px;top:48px;font-size:11px;line-height:18px;text-align:center;width:118px}
.who b{font-weight:700;letter-spacing:.2px}
.who i{display:block}
.quote{position:absolute;left:11px;top:126px;width:215px;font-size:10.4px;line-height:15px}
.testimonial .btn{left:144px;top:176px;width:67px;background:var(--purple)}

.newsletter-back{left:276px;top:932px;width:232px;height:206px;background:var(--lime);transform:rotate(2deg)}
.newsletter{left:270px;top:930px;width:229px;height:208px;background:var(--green)}
.field{width:197px;height:24px;background:var(--field);color:#777;font-size:10px;padding:5px 7px;margin-bottom:9px}
.field.msg{height:67px}
.newsletter .btn{left:142px;top:178px;width:68px;background:var(--blue)}

.news-back{left:530px;top:934px;width:232px;height:206px;background:var(--lime);transform:rotate(2.2deg)}
.news{left:522px;top:928px;width:231px;height:208px;background:var(--orange);transform:rotate(-0.8deg)}
.news-item{position:absolute;left:8px;width:212px;height:56px}
.news-item.i1{top:35px}
.news-item.i2{top:106px}
.news-sep{position:absolute;left:8px;top:95px;width:212px;height:1px;background:rgba(255,255,255,.7)}
.date{position:absolute;left:0;top:0;width:58px;height:45px;border:2px solid #fff;border-radius:3px;display:flex;align-items:center}
.date .d{width:26px;text-align:center;font-size:16px;font-weight:700;border-right:2px solid #fff;height:100%;line-height:40px}
.date .m{flex:1;text-align:center;font-size:9px;font-style:italic;line-height:11px}
.news-text{position:absolute;left:70px;top:0;font-size:10.5px;line-height:15px}
.news-text .time{font-style:italic;font-weight:600;font-size:10px;display:flex;align-items:center;gap:4px}
.news .btn{left:148px;top:180px;width:66px;background:var(--pink)}

/* footer */
.footer{left:0;top:1170px;width:778px;height:30px;background:var(--navy);color:#fff;font-size:10.5px;display:flex;justify-content:space-between;align-items:center;padding:0 14px 0 15px}
.footer nav span{margin-right:6px}
.footer nav .current{color:var(--orange)}
</style>
</head>
<body>
<div class="site">

  <header>
    <div class="abs brand">Sproutyard</div>

    <div class="ph" role="img" aria-label="Photo of a little girl reading a book" style="left:284px;top:17px;width:87px;height:124px;background:linear-gradient(180deg,#d9b49a,#d9493f 55%,#e8d9c8);border-radius:40px 40px 10px 10px"></div>
    <div class="ph" role="img" aria-label="Pink butterfly illustration" style="left:403px;top:12px;width:48px;height:42px;background:#f2a6cf;border-radius:50%"></div>
    <div class="ph" role="img" aria-label="Spotted butterfly illustration" style="left:471px;top:14px;width:69px;height:60px;background:#f4bde0;border-radius:50%"></div>
    <div class="ph" role="img" aria-label="Smiling sun illustration" style="left:556px;top:14px;width:50px;height:50px;background:#fbd54a;border-radius:50%"></div>
    <div class="ph" role="img" aria-label="Photo of a sitting baby" style="left:716px;top:24px;width:50px;height:66px;background:linear-gradient(180deg,#c98f6d,#e2b295);border-radius:20px"></div>

    <div class="abs social" aria-label="Social links">
      <span class="s1" role="img" aria-label="chatterdeck"></span>
      <span class="s2" role="img" aria-label="quibbly"></span>
      <span class="s3" role="img" aria-label="snapwheel"></span>
    </div>
    <div class="abs member-login">Member Login</div>

    <nav class="nav">
      <div class="tab home">Home</div>
      <div class="tab about">About</div>
      <div class="tab activities">Activities</div>
      <div class="tab services">Services</div>
      <div class="tab contact">Contact</div>
    </nav>
  </header>

  <div class="ph hero" role="img" aria-label="Hero photo of laughing children at the fun centre"></div>
  <svg class="hero-curve" width="778" height="48" viewBox="0 0 778 48" aria-hidden="true">
    <path d="M0 0H778V0C700 18 600 28 500 24C400 20 300 14 200 22C120 28 60 42 0 44Z" fill="#ffffff"/>
  </svg>
  <div class="ph hanging-kid" role="img" aria-label="Photo of a child jumping and hanging from the menu"></div>

  <section>
    <h1 class="abs welcome-title">Welcome to Sproutyard</h1>
    <div class="abs welcome-rule"></div>
    <div class="abs welcome-copy">
      <p><b>Lorem ipsum dolor sit amet, consectetur adipiscing elit.</b> Maecenas gravida auctor nulla, at scelerisque lorem Fermentum et. Donec venenatis, dolor id facilisis gravida, libero enim ultricies arcu, At consequat magna risus vel Arculiquam eu ligula commodo, tempus mi non, tempor ante.</p>
      <p><b>Nullam malesuada velit a rhoncus porta.</b> Lorem ipsum dolor sit amet, consectetur adipiscing elit. Maecenas Gravida auctor nulla, at scelerisque lorem fermentum et. Donec venenatis.</p>
      <p>Dolor id facilisis gravida.Lorem ipsum dolor sit amet, consectetur adipiscing elit. Maecenas gravida auctor nulla.</p>
    </div>
    <div class="abs welcome-photo"><div role="img" aria-label="Photo of a teacher with children at a table"></div></div>
  </section>

  <section>
    <h2 class="abs fun-title">Sproutyard - Fun Centre for Childrens Development</h2>
    <div class="abs thumbs">
      <div class="thumb"><div class="pic"><div class="t1" role="img" aria-label="Photo of a teacher with children"></div></div><p>Closer teachers &amp; child.</p></div>
      <div class="thumb"><div class="pic"><div class="t2" role="img" aria-label="Photo of two children lying on grass"></div></div><p>Quiet atmosphere</p></div>
      <div class="thumb"><div class="pic"><div class="t3" role="img" aria-label="Photo of a child playing piano"></div></div><p>Children Activities</p></div>
      <div class="thumb"><div class="pic"><div class="t4" role="img" aria-label="Photo of children raising hands in class"></div></div><p>Children Activities</p></div>
      <div class="thumb"><div class="pic"><div class="t5" role="img" aria-label="Photo of children at computers"></div></div><p>Learn Computer Skills</p></div>
    </div>
  </section>

  <section>
    <div class="card-back testimonial-back"></div>
    <div class="card testimonial">
      <h2>Testimonilas</h2>
      <div class="avatar" role="img" aria-label="Photo of a parent with children"></div>
      <div class="who"><b>MIRA CASTELL</b><i>(Care Centre Admin)</i><i>Posted on monday</i></div>
      <p class="quote">Lorem ipsum dolor sit amet, consectetur adip iscing elit. Maecenas gravida auctor nulla, at scelerisque lorem ferme.</p>
      <div class="btn">View All</div>
    </div>

    <div class="card-back newsletter-back"></div>
    <div class="card newsletter">
      <h2>Newsletters</h2>
      <div class="field">Name:</div>
      <div class="field">Email Address:</div>
      <div class="field msg">Massage</div>
      <div class="btn">Sing up</div>
    </div>

    <div class="card-back news-back"></div>
    <div class="card news">
      <h2>Latest News</h2>
      <div class="news-item i1">
        <div class="date"><span class="d">25</span><span class="m">Mar<br>2014</span></div>
        <div class="news-text">Entertainment<span class="time"><svg width="9" height="9" viewBox="0 0 10 10"><circle cx="5" cy="5" r="4" fill="none" stroke="#fff" stroke-width="1.2"/><path d="M5 2.5V5H7" fill="none" stroke="#fff" stroke-width="1.2"/></svg>11:00 PM to 7 : 00 pm</span>Lorem consec adipiscing elit.</div>
      </div>
      <div class="news-sep"></div>
      <div class="news-item i2">
        <div class="date"><span class="d">25</span><span class="m">Mar<br>2014</span></div>
        <div class="news-text">Entertainment<span class="time"><svg width="9" height="9" viewBox="0 0 10 10"><circle cx="5" cy="5" r="4" fill="none" stroke="#fff" stroke-width="1.2"/><path d="M5 2.5V5H7" fill="none" stroke="#fff" stroke-width="1.2"/></svg>11:00 PM to 7 : 00 pm</span>Lorem consec adipiscing elit.</div>
      </div>
      <div class="btn">View All</div>
    </div>
  </section>

  <footer class="abs footer">
    <nav><span class="current">Home</span><span>/</span><span>About us</span><span>/</span><span>Activities</span><span>/</span><span>Facality</span><span>/</span><span>Contact&nbsp; Us</span></nav>
    <div>Copyright © 2014 Sproutyard. All Rights Reserved</div>
  </footer>

</div>
</body>
</html>
```